Bref créative
Corporate Advisory
Professional
Dorian Pelhame
Director
Level 6, 412 Brindle Street, Marlow Heights. NSW 2710
dorian.pelhame@veltrina.com.au
www.veltrina.com.au
Corporate colours are the blue and white in logo. Front may be one colour eg white with blue logo and rear may be blue with white logo
Can be as simple as blue background and white logo
Veltrina logo - white background with blue logo is primary and blue background with white logo is secondary - no other coloures used.

```html
<!DOCTYPE html>
<html lang="en">
<head>
<meta charset="utf-8">
<title>Veltrina Stationery</title>
<link href="https://fonts.googleapis.com/css2?family=Josefin+Sans:wght@300;400;600&display=swap" rel="stylesheet">
<style>
  :root {
    --navy: #1f3a5a;
    --white: #ffffff;
    --paper-shadow: rgba(0,0,0,0.18);
    --stage: #dcdcd9;
    --tone-light: #e4e4e6;
    --text-grey: #6b7480;
    --font: "Josefin Sans", sans-serif;
  }
  * { box-sizing: border-box; margin: 0; padding: 0; }
  html, body { width: 1200px; height: 871px; overflow: hidden; }
  body { background: var(--stage); font-family: var(--font); color: var(--navy); position: relative; }
  .sheet { position: absolute; background: var(--white); box-shadow: 0 3px 10px var(--paper-shadow); }

  /* Brand lockup */
  .brand { display: flex; align-items: flex-start; gap: 8px; }
  .brand-mark { width: 22px; height: 22px; background: var(--navy); flex: none; margin-top: 2px; }
  .brand-name { font-weight: 400; font-size: 30px; letter-spacing: 1px; line-height: 1; text-transform: uppercase; white-space: nowrap; }
  .brand-tagline { font-size: 6.5px; letter-spacing: 0.6px; text-transform: uppercase; margin-top: 3px; color: var(--text-grey); white-space: nowrap; }
  .brand--light { color: var(--white); }
  .brand--light .brand-mark { background: var(--white); }
  .brand--light .brand-tagline { color: var(--white); opacity: 0.85; }

  .small-print { font-size: 7px; line-height: 1.55; color: var(--text-grey); white-space: nowrap; }
  .small-print b { font-weight: 600; color: var(--navy); display: inline-block; width: 30px; }

  /* Business card front */
  .card-front { left: 240px; top: 65px; width: 284px; height: 132px; padding: 12px 14px; }
  .card-front .holder { text-align: right; font-size: 9px; color: var(--navy); }
  .card-front .holder span { color: var(--text-grey); }
  .card-front .brand { margin-top: 4px; }
  .card-front .brand-name { font-size: 22px; }
  .card-front .brand-mark { width: 17px; height: 17px; }
  .card-front .small-print { margin-top: 7px; margin-left: 25px; font-size: 6px; line-height: 1.5; }

  /* Business card back */
  .card-back { left: 240px; top: 217px; width: 284px; height: 137px; background: var(--navy);
    display: flex; flex-direction: column; align-items: center; justify-content: center; }
  .card-back .brand-name { font-size: 24px; }
  .card-back .web { position: absolute; bottom: 12px; left: 0; right: 0; text-align: center;
    font-size: 6.5px; color: var(--white); opacity: 0.8; letter-spacing: 0.5px; }

  /* Letterhead */
  .letterhead { left: 541px; top: 43px; width: 601px; height: 787px; }
  .letterhead .brand { position: absolute; left: 36px; top: 64px; }
  .letterhead .address { position: absolute; left: 318px; top: 22px; width: 130px; font-size: 7px; line-height: 1.5; color: var(--text-grey); }
  .letterhead .contact { position: absolute; left: 481px; top: 22px; }
  .letterhead .tone-block { position: absolute; right: 0; top: 335px; width: 103px; height: 175px; background: var(--tone-light); }
  .letterhead .feature-frame { position: absolute; right: 0; bottom: 0; width: 332px; height: 339px;
    background: var(--white); border: 8px solid var(--tone-light); }
  .letterhead .feature-art { position: absolute; left: 70px; right: 70px; top: 34px; bottom: 30px;
    background: linear-gradient(180deg, #dadadd, #c4c4c8); border-radius: 40% 40% 6px 6px; }

  /* Envelope */
  .envelope { left: 53px; top: 400px; width: 673px; height: 406px; z-index: 2; }
  .envelope .flap { position: absolute; left: 0; top: 0; width: 100%; height: 150px; background: var(--navy);
    clip-path: polygon(0 0, 100% 5%, 100% 100%, 0 100%); display: flex; justify-content: center; align-items: center; }
  .envelope .flap .brand { transform: rotate(180deg); }
  .envelope .flap .brand-name { font-size: 26px; }
  .envelope .sender { position: absolute; left: 31px; top: 177px; }
  .envelope .sender .brand-name { font-size: 28px; }
  .envelope .sender .small-print { margin-top: 10px; margin-left: 30px; }
  .envelope .feature-frame { position: absolute; left: 481px; top: 221px; width: 168px; height: 178px;
    border: 6px solid var(--tone-light); background: var(--white); }
  .envelope .feature-art { position: absolute; left: 30px; right: 30px; top: 18px; bottom: 14px;
    background: linear-gradient(180deg, #dadadd, #c4c4c8); border-radius: 40% 40% 4px 4px; }
</style>
</head>
<body>

  <section class="sheet card-front" aria-label="Business card front">
    <p class="holder">Dorian Pelhame <span>| Director</span></p>
    <div class="brand">
      <span class="brand-mark"></span>
      <div>
        <div class="brand-name">Veltrina</div>
        <div class="brand-tagline">Advisory built on steady trust</div>
      </div>
    </div>
    <div class="small-print">
      Level 6, 412 Brindle Street, Marlow Heights. NSW 2710<br>
      <b>Phone</b> +61 2 4000 0000<br>
      <b>Fax</b> +61 2 4000 0001<br>
      <b>Mobile</b> 0400 000 000<br>
      <b>Email</b> dorian.pelhame@veltrina.com.au<br>
      <b>Web</b> www.veltrina.com.au
    </div>
  </section>

  <section class="sheet card-back" aria-label="Business card back">
    <div class="brand brand--light">
      <span class="brand-mark"></span>
      <div>
        <div class="brand-name">Veltrina</div>
        <div class="brand-tagline">Advisory built on steady trust</div>
      </div>
    </div>
    <p class="web">www.veltrina.com.au</p>
  </section>

  <section class="sheet letterhead" aria-label="Letterhead">
    <div class="brand">
      <span class="brand-mark"></span>
      <div>
        <div class="brand-name">Veltrina</div>
        <div class="brand-tagline">Advisory built on steady trust</div>
      </div>
    </div>
    <p class="address">Level 6, 412 Brindle Street, Marlow Heights. NSW 2710</p>
    <div class="small-print contact">
      <b>Phone</b> +61 2 4000 0000<br>
      <b>Fax</b> +61 2 4000 0001
    </div>
    <div class="tone-block"></div>
    <div class="feature-frame">
      <div class="feature-art" role="img" aria-label="Large faint grey chess knight piece decoration"></div>
    </div>
  </section>

  <section class="sheet envelope" aria-label="Envelope">
    <div class="flap">
      <div class="brand brand--light">
        <span class="brand-mark"></span>
        <div><div class="brand-name">Veltrina</div></div>
      </div>
    </div>
    <div class="sender">
      <div class="brand">
        <span class="brand-mark"></span>
        <div>
          <div class="brand-name">Veltrina</div>
          <div class="brand-tagline">Advisory built on steady trust</div>
        </div>
      </div>
      <div class="small-print">
        Level 6, 412 Brindle Street, Marlow Heights. NSW 2710<br>
        <b>Phone</b> +61 2 4000 0000<br>
        <b>Fax</b> +61 2 4000 0001<br>
        <b>Email</b> dorian.pelhame@veltrina.com.au<br>
        <b>Web</b> www.veltrina.com.au
      </div>
    </div>
    <div class="feature-frame">
      <div class="feature-art" role="img" aria-label="Faint grey chess knight piece decoration"></div>
    </div>
  </section>

</body>
</html>
```